Web Site for Strategy and Technology Consulting Company

We are looking for a website design that engages potential customers to understand our services and contact us. In this contest, we are looking for a homepage design, but the winning designer will be favored for the design of some of the more complicated interior pages of the site. An additional contest (or contests) for these pages will be added soon.

PLATROM AND RESPONSIVE DESIGN
The site will be implemented in WordPress using the Elementor page builder.
We are looking for a design that will look good on phones are well as laptop browsers.

UPLOADED FILES INCLUDE:
1a A wireframe of the homepage we are looking for. The Uploaded PDF also includes a draft of the text proposed for the homepage. Designers are free to go beyond the wireframe, but all elements of the wireframe should be included.
1b A Word document with the draft text of the homepage.
2a-d The Norvalith logo. Two versions are included – a dark version which works well against a light background, and a light version which works well against a dark background.
3 The Norvalith color palette with HEX and RGB values. Designers are not limited to this palette, but colors should be complementary.
4 A draft of the homepage menu
5 Service sheets with information on the services we provide

MORE ABOUT NORVALITH
Norvalith is a consulting company focused on transforming businesses through software. Our tagline, “Transformation Delivered,” recognizes the gap business often have between business transformation and the software they end up with. By listening to our customers and understanding their vision and where they are, we help get our customers where they want to go.

We increase our capability by working with many consultants and partners, allowing us to provide our customers with the best people and the software that best suits them.

Industry/Entity Type

Consulting

Number of Pages Required

1 page

Font styles to use
Sans Serif

Requirements
Must have
• the content represented on the wireframe uploaded
Nice to have
• interactive features, such as roll-over icons that reveal additional information

```html
<!DOCTYPE html>
<html lang="en">
<head>
<meta charset="utf-8">
<title>Norvalith – Transformation Delivered</title>
<link href="https://fonts.googleapis.com/css2?family=Roboto:wght@400;500;700&display=swap" rel="stylesheet">
<style>
:root{
  --navy:#3d4b66;
  --text:#5a6070;
  --yellow:#e0b615;
  --blue:#1f5f99;
  --blue-light:#a6b4f5;
  --grey-bg:#f7f7f7;
  --footer:#435470;
  --white:#ffffff;
}
*{margin:0;padding:0;box-sizing:border-box}
html,body{width:1200px;height:3292px;overflow:hidden}
body{font-family:'Roboto',Arial,sans-serif;color:var(--text);background:var(--white);position:relative}
.abs{position:absolute}
h2.title{font-weight:700;color:var(--navy);text-transform:uppercase;line-height:1.08}
.rule{display:block;width:62px;height:4px;background:var(--yellow)}
.btn{position:absolute;display:flex;align-items:center;justify-content:center;font-size:13px;font-weight:700;text-transform:uppercase;color:var(--white);background:var(--yellow)}
.btn.outline{background:transparent;border:2px solid var(--yellow);color:var(--navy)}
p{font-size:14.5px;line-height:1.5}

/* header */
.site-header{left:89px;top:14px;width:1023px;height:57px;background:var(--white);box-shadow:0 4px 18px rgba(0,0,0,.06)}
.brand{left:22px;top:10px;font-size:34px;color:#6a6a6a;font-weight:400}
.nav{right:176px;top:0;height:57px;display:flex;gap:30px;align-items:center;font-size:13px;font-weight:500;color:var(--navy)}
.nav-cta{right:0;top:0;width:143px;height:57px}

/* hero */
.hero{left:0;top:0;width:1200px;height:721px;background:var(--grey-bg)}
.hero h1{left:89px;top:211px;font-size:46px;font-weight:700;color:var(--navy);line-height:1.1}
.hero .rule{position:absolute;left:89px;top:317px;width:56px}
.hero .intro{left:89px;top:335px;width:680px;font-size:14px}
.hero ul{left:89px;top:413px;list-style:none;font-size:14px;line-height:21.5px}
.hero li{padding-left:18px;position:relative}
.hero li:before,.people li:before{content:"";position:absolute;left:0;top:8px;width:7px;height:7px;border-radius:50%;background:var(--yellow)}
.hero .close{left:89px;top:508px;font-size:14px}
.hero-art{left:665px;top:211px;width:447px;height:415px;border-radius:6px;background:linear-gradient(135deg,#d8d8d8 0%,#8a8a8a 45%,#2d62a0 75%,#a6b4f5 100%);opacity:.85}

/* intro */
.support h2{left:168px;top:843px;font-size:36px}
.support .rule{position:absolute;left:168px;top:966px}
.support p{left:583px;top:843px;width:420px;font-size:14px}
.support .btn{left:583px;top:967px;width:147px;height:40px}

/* services */
.card{top:1089px;width:198px;height:223px;background:var(--white);box-shadow:0 8px 26px rgba(0,0,0,.08)}
.card .icon{position:absolute;left:36px;top:46px;width:70px;height:62px;border-radius:8px;background:linear-gradient(135deg,#dce6f3,#b9cde6)}
.card h3{position:absolute;left:36px;top:152px;font-size:17px;font-weight:500;color:var(--navy);line-height:1.3}
.card.featured{background:var(--yellow);color:var(--white)}
.card.featured h3{color:var(--white);top:74px;left:22px;font-size:17px}
.card.featured p{position:absolute;left:22px;top:125px;width:150px;font-size:12.5px;line-height:1.4}
.services-note{left:0;top:1346px;width:1200px;text-align:center;font-size:14px}

/* people */
.people{left:0;top:1459px;width:1200px;height:595px;background:linear-gradient(180deg,#21609a 0%,#1f62a0 60%,#2a78bd 100%)}
.people-art{left:115px;top:100px;width:428px;height:409px;border-radius:6px;background:linear-gradient(160deg,#ffffff 0%,#c9d6e6 45%,#6f8eb0 100%);opacity:.9}
.people h2{left:608px;top:134px;font-size:37px;color:var(--white)}
.people .rule{position:absolute;left:608px;top:181px;width:46px}
.people .txt{left:608px;top:194px;width:455px;color:var(--white);font-size:14px}
.people ul{left:608px;top:297px;width:470px;list-style:none;color:var(--white);font-size:14px;line-height:21.5px}
.people li{position:relative;padding-left:16px}
.people .txt2{left:608px;top:372px;width:455px;color:var(--white);font-size:14px}
.people .btn{left:609px;top:438px;width:127px;height:39px}

/* reviews */
.reviews h2{left:189px;top:2185px;font-size:37px}
.reviews .rule{position:absolute;left:189px;top:2280px}
.review-box{left:464px;top:2189px;width:549px;height:303px;border:2px solid #c5d9ee}
.quote{font-size:110px;font-weight:700;color:#a9c6ea;line-height:1;font-family:Georgia,serif}
.q-open{left:522px;top:2150px}
.q-close{left:925px;top:2445px}
.review-box p{position:absolute;left:64px;top:64px;width:420px;font-size:14px}
.review-box .who{position:absolute;left:64px;top:160px;font-size:14px;font-weight:500;color:var(--navy)}
.review-box .org{position:absolute;left:64px;top:180px;font-size:12.5px}
.arrow{position:absolute;top:220px;width:40px;height:40px;border-radius:50%;display:flex;align-items:center;justify-content:center}
.arrow.prev{left:64px;background:var(--blue)}
.arrow.next{left:110px;background:var(--yellow)}

/* technologies */
.tech h2{left:189px;top:2594px;font-size:37px}
.tech .rule{position:absolute;left:189px;top:2645px}
.tech-list{left:189px;top:2686px;width:830px;display:flex;justify-content:space-between;align-items:center}
.tech-item{display:flex;align-items:center;gap:7px;font-size:20px;font-weight:500;color:#4a5568}
.tech-item i{display:block;width:16px;height:16px;background:var(--blue);border-radius:50%}

/* footer */
.footer{left:0;top:2814px;width:1200px;height:478px;background:var(--footer);color:var(--white)}
.footer .brand-lg{left:120px;top:208px;font-size:50px;color:#e9edf3}
.footer h4{font-size:20px;font-weight:700;text-transform:uppercase}
.links{left:415px;top:140px}
.links ul{list-style:none;margin-top:14px;font-size:16px;line-height:31px}
.contact{left:653px;top:140px}
.contact ul{list-style:none;margin-top:14px;font-size:16px;line-height:31px}
.contact li{display:flex;gap:8px;align-items:flex-start}
.contact svg{margin-top:10px;flex:none}
.contact .indent{padding-left:19px}
.map{left:636px;top:188px;width:290px;height:140px;border-radius:40px;background:radial-gradient(ellipse at center,rgba(255,255,255,.12),rgba(255,255,255,0) 70%)}
.social{top:224px;width:34px;height:34px;border-radius:50%;background:rgba(255,255,255,.2)}
.divider{left:89px;top:420px;width:1023px;height:1px;background:rgba(255,255,255,.25)}
.to-top{left:1112px;top:401px;width:40px;height:40px;border-radius:50%;background:var(--blue);display:flex;align-items:center;justify-content:center}
.copyright{left:0;top:443px;width:1200px;text-align:center;font-size:14px}
</style>
</head>
<body>

<section class="hero abs">
  <div class="abs hero-art" role="img" aria-label="Large grey brand letterform with scattered blue and yellow squares"></div>
  <h1 class="abs">TRANSFORMATION<br>DELIVERED.</h1>
  <span class="rule"></span>
  <p class="abs intro">We do more for our customers than implement software. We listen. We work to understand where they are in their transformation journey and where they want to go. We partner with them to clear the roadblocks that stand in their way, ensuring they reach their destination. At Norvalith, we:</p>
  <ul class="abs">
    <li>Focus on business value, with an emphasis on delivering value quickly.</li>
    <li>Meet our customers where they are without backing them up to the beginning of their journey.</li>
    <li>Provide a wide range of services, from strategy to product support.</li>
    <li>Commit to our customer's long-term success.</li>
  </ul>
  <p class="abs close">Norvalith is business transformation, delivered.</p>
  <a class="btn" style="left:89px;top:544px;width:126px;height:40px">Our Story</a>
</section>

<header class="site-header abs">
  <div class="abs brand">Norvalith</div>
  <nav class="abs nav"><span>ABOUT US</span><span>SERVICES</span><span>INSIGHTS</span><span>JOIN US</span></nav>
  <a class="btn nav-cta">Contact Us</a>
</header>

<section class="support">
  <h2 class="title abs">Transformation<br>supported by<br>technology</h2>
  <span class="rule"></span>
  <p class="abs">During our early years, Norvalith focused only on business transformation. We came to realize that successful transformation often depended on quality software implementations, and often more than one. Now we focus on five things, the five things most businesses need to reach their goals.</p>
  <a class="btn outline">How We Work</a>
</section>

<section class="services">
  <div class="card abs" style="left:87px"><div class="icon" role="img" aria-label="Globe with network icon"></div><h3>Business<br>Transformation</h3></div>
  <div class="card abs" style="left:293px"><div class="icon" role="img" aria-label="Monitor with chart icon"></div><h3>ERP<br>Imlementations</h3></div>
  <div class="card abs" style="left:499px"><div class="icon" role="img" aria-label="Customer and data icon"></div><h3>CRM<br>Imlementations</h3></div>
  <div class="card abs" style="left:706px"><div class="icon" role="img" aria-label="Dashboard monitor icon"></div><h3>BI<br>and Data</h3></div>
  <div class="card featured abs" style="left:912px"><h3>Building the right<br>team of people</h3><p>Hire resources for your transformation journey.</p></div>
  <p class="abs services-note">Find out how Norvalith can help you put all the pieces together and get them done.</p>
</section>

<section class="people abs">
  <div class="abs people-art" role="img" aria-label="White brand letterform surrounded by team member portraits"></div>
  <h2 class="title abs">It's the people</h2>
  <span class="rule"></span>
  <p class="abs txt">The world has changed in the past twenty years. The people you need might not all work for one company. Our clients want the best resources, available quickly. That's why, in addition to our team of experts, we partner with:</p>
  <ul class="abs">
    <li>A large network of expert consultants who are the best at what they do,</li>
    <li>Service providers all over the world to provide the resources and value that are right for you, available 24 x 7.</li>
  </ul>
  <p class="abs txt2">People are invariably at the center of our customer's success. Find out how we can add our experts to yours.</p>
  <a class="btn">Our Team</a>
</section>

<section class="reviews">
  <h2 class="title abs">Customers<br>reviews</h2>
  <span class="rule"></span>
  <div class="abs review-box">
    <p>Norvalith quickly moved us past talking about what needed to be done, to doing it. Development projects are never easy and when things got tough in the first phase of development, Norvalith stepped in to right the ship and put us on a new course.</p>
    <div class="who">Dana Whitfield, President</div>
    <div class="org">Brightline Fixture Works</div>
    <span class="arrow prev"><svg width="10" height="10" viewBox="0 0 10 10"><path d="M6 2 3 5l3 3" stroke="#fff" stroke-width="1.6" fill="none"/></svg></span>
    <span class="arrow next"><svg width="10" height="10" viewBox="0 0 10 10"><path d="M4 2l3 3-3 3" stroke="#fff" stroke-width="1.6" fill="none"/></svg></span>
  </div>
  <div class="abs quote q-open">&ldquo;</div>
  <div class="abs quote q-close">&rdquo;</div>
</section>

<section class="tech">
  <h2 class="title abs">Technologies</h2>
  <span class="rule"></span>
  <div class="abs tech-list">
    <span class="tech-item"><i></i>Corevia Suite</span>
    <span class="tech-item">Ledgerly</span>
    <span class="tech-item">Stratus Cloud</span>
    <span class="tech-item">Peoplegrid</span>
    <span class="tech-item">Viewmetric</span>
    <span class="tech-item"><i></i>Frostbase</span>
  </div>
</section>

<footer class="footer abs">
  <div class="abs brand-lg">Norvalith</div>
  <div class="abs map" role="img" aria-label="Faint dotted world map"></div>
  <div class="abs links">
    <h4>Useful links</h4>
    <ul><li>Offerings</li><li>Capabilities</li><li>Industries</li><li>Team</li><li>About</li></ul>
  </div>
  <div class="abs contact">
    <h4>Contact us</h4>
    <ul>
      <li><svg width="11" height="13" viewBox="0 0 11 13"><path d="M5.5 0A4.5 4.5 0 0 0 1 4.5C1 8 5.5 13 5.5 13S10 8 10 4.5A4.5 4.5 0 0 0 5.5 0zm0 6.3a1.8 1.8 0 1 1 0-3.6 1.8 1.8 0 0 1 0 3.6z" fill="#fff"/></svg>48 Harborview Plaza</li>
      <li class="indent">Suite 210, Lakeport, MN 55900</li>
      <li><svg width="12" height="12" viewBox="0 0 12 12"><path d="M2.5 0 4.6 2.7 3.4 4.2a8 8 0 0 0 4.4 4.4l1.5-1.2L12 9.5 10.6 12C5 11.6.4 7 0 1.4z" fill="#fff"/></svg>(555) 018-2740</li>
      <li><svg width="12" height="10" viewBox="0 0 12 10"><path d="M0 0h12v10H0z" fill="#fff"/><path d="M0 0l6 5 6-5" stroke="#435470" fill="none"/></svg>Email Us</li>
    </ul>
  </div>
  <span class="abs social" style="left:993px"></span>
  <span class="abs social" style="left:1035px"></span>
  <div class="abs divider"></div>
  <span class="abs to-top"><svg width="10" height="10" viewBox="0 0 10 10"><path d="M2 6l3-3 3 3" stroke="#fff" stroke-width="1.6" fill="none"/></svg></span>
  <p class="abs copyright">&copy; 2023 Norvalith Consulting | All Rights Reserved</p>
</footer>

</body>
</html>
```